Create a professional, eye-catching business card design that reflects the values and services of Brookfern Veterinary Hospital. we provide veterinary services and the business card should be a memorable representation of the clinic and align with its branding and mission. our tag line is "Trusted Friends, Gentle Expert Care"
Use clean, modern typography. Prioritize readability and professionalism. We would like to see designs that use the color blue, as in the logo example. the final design should communicate professionalism and care, with attention to detail.

```html
<!DOCTYPE html>
<html lang="en">
<head>
<meta charset="utf-8">
<title>Brookfern Veterinary Hospital – Business Card</title>
<link href="https://fonts.googleapis.com/css2?family=Montserrat:wght@500;800&family=Roboto:wght@400;500&family=Dancing+Script:wght@500&display=swap" rel="stylesheet">
<style>
  :root {
    --navy: #1f3160;
    --navy-soft: #2c4177;
    --white: #ffffff;
    --pale: #eef1f7;
    --ink: #3a3a3a;
    --stage: #1c1c1e;
  }
  * { box-sizing: border-box; margin: 0; padding: 0; }
  html, body { width: 1200px; height: 900px; overflow: hidden; }
  body {
    background: var(--stage);
    display: flex;
    flex-direction: column;
    align-items: center;
    justify-content: center;
    gap: 44px;
    font-family: "Roboto", Arial, sans-serif;
  }
  .card {
    position: relative;
    width: 660px;
    height: 377px;
    overflow: hidden;
    border-radius: 4px;
    box-shadow: 0 10px 30px rgba(0,0,0,.5);
  }

  /* Front */
  .card-front { background: var(--white); }
  .front-shapes { position: absolute; inset: 0; }
  .brand-name {
    position: absolute; left: 44px; top: 28px;
    color: var(--navy);
    font-family: "Montserrat", Arial, sans-serif;
    font-weight: 800;
    line-height: 1;
  }
  .brand-name .brand-main { display: block; font-size: 46px; letter-spacing: 1px; }
  .brand-name .brand-sub { display: block; font-size: 15px; letter-spacing: 1.6px; margin-top: 4px; }
  .person { position: absolute; left: 44px; top: 118px; }
  .person-name {
    font-family: "Montserrat", Arial, sans-serif;
    font-weight: 800; font-size: 19px; color: var(--navy); letter-spacing: .5px;
  }
  .person-role { font-size: 16px; color: var(--ink); margin-top: 3px; }
  .contact { position: absolute; left: 44px; top: 184px; list-style: none; }
  .contact li {
    display: flex; align-items: center; gap: 8px;
    font-size: 15px; color: var(--ink); line-height: 23px;
  }
  .contact svg { width: 13px; height: 13px; fill: var(--navy); flex: none; }
  .art-area {
    position: absolute; left: 395px; top: 100px;
    width: 220px; height: 220px; border-radius: 50%;
    background: linear-gradient(180deg, var(--pale) 0%, var(--pale) 50%, var(--navy-soft) 100%);
    border: 2px solid var(--navy);
  }
  .address {
    position: absolute; right: 36px; bottom: 18px;
    color: var(--white); font-size: 15px; line-height: 20px; text-align: right;
  }

  /* Back */
  .card-back {
    background: var(--navy);
    display: flex; flex-direction: column; align-items: center; justify-content: center;
    color: var(--white);
  }
  .back-brand {
    font-family: "Montserrat", Arial, sans-serif;
    font-weight: 800; text-align: center; line-height: 1;
  }
  .back-brand .brand-main { display: block; font-size: 54px; letter-spacing: 1px; }
  .back-brand .brand-sub { display: block; font-size: 17px; letter-spacing: 2px; margin-top: 6px; }
  .tagline {
    font-family: "Dancing Script", cursive;
    font-weight: 500; font-size: 30px; margin-top: 26px;
  }
  .tagline-rule { width: 210px; height: 14px; margin-top: 2px; align-self: center; transform: translateX(40px); }
</style>
</head>
<body>

  <section class="card card-front" aria-label="Business card front">
    <svg class="front-shapes" viewBox="0 0 660 377" preserveAspectRatio="none" aria-hidden="true">
      <path d="M0,175 C10,290 180,320 420,350 L560,300 L660,250 L660,377 L0,377 Z" fill="var(--navy)"/>
      <path d="M18,170 C30,280 190,310 415,335" fill="none" stroke="var(--white)" stroke-width="4"/>
    </svg>

    <div class="brand-name">
      <span class="brand-main">BROOKFERN</span>
      <span class="brand-sub">VETERINARY HOSPITAL</span>
    </div>

    <div class="person">
      <p class="person-name">DANIEL MARSH</p>
      <p class="person-role">Managing Director</p>
    </div>

    <ul class="contact">
      <li><svg viewBox="0 0 24 24"><path d="M6.6 10.8a15 15 0 0 0 6.6 6.6l2.2-2.2a1 1 0 0 1 1-.25 11.4 11.4 0 0 0 3.6.57 1 1 0 0 1 1 1V20a1 1 0 0 1-1 1A17 17 0 0 1 3 4a1 1 0 0 1 1-1h3.5a1 1 0 0 1 1 1c0 1.25.2 2.45.57 3.57a1 1 0 0 1-.25 1z"/></svg>044-555 210 347</li>
      <li><svg viewBox="0 0 24 24"><path d="M2 5h20v14H2zm2 2v.5l8 5 8-5V7l-8 5z"/></svg>info@brookfernvet.com</li>
      <li><svg viewBox="0 0 24 24"><circle cx="12" cy="12" r="10"/></svg>www.brookfernvet.com</li>
    </ul>

    <div class="art-area" role="img" aria-label="Illustration of two pets sitting on a hill beneath a leafy branch"></div>

    <p class="address">Your Address, City<br>State, Zip 0000</p>
  </section>

  <section class="card card-back" aria-label="Business card back">
    <div class="back-brand">
      <span class="brand-main">BROOKFERN</span>
      <span class="brand-sub">VETERINARY HOSPITAL</span>
    </div>
    <p class="tagline">Trusted Friends, Gentle Expert Care</p>
    <svg class="tagline-rule" viewBox="0 0 210 14" aria-hidden="true">
      <path d="M0,4 C70,6 140,9 210,13 C140,11 70,9 0,6 Z" fill="var(--white)"/>
    </svg>
  </section>

</body>
</html>
```